World travel poster - I want to remember where I've been!

I would like a poster for me to print and keep in my home as a record of my world travels. It must look like a mechanical sign in an airport (see picture for example) However I am flexible with exact layout, if you'd like to add images used to enhance poster etc. I have also uploaded some pictures from my travels if you would like to use some or all of them. They are named according to location.

Poster must include:
USA 2003
Malaysia 2006
Thailand 2007
Italy 2009
India, Vietnam, Hong Kong 2010
Bali 2011
Malaysia 2012
Singapore 2012
Vietnam, Cambodia, Laos 2013
Europe 2015

and the quote:

"The world is a book and those who do not travel read only one page."
― Severin of Tallowmere
Updates

Hi there. I have uploaded some photos of my travels to possibly use in my poster. They are named according to location. I haven't decided if I prefer the originial layout or with images, so please post both for me to consider. Thanks so much for your time to consider my project.

Target Market(s)

Something to catch the eye of visitors and remind me of my adventures.
A classic piece that is a conversation starter.

Industry/Entity Type

Airport

Other font styles liked:
• Airport mechanical font

Requirements
Must have
• Some lettering like a mechanical airport board (see image attached for example).
Dimensions that are easy to print - either A3, or a long/narrow poster.
Nice to have
• A splash of colour or an image, maybe the words 'arrivals' or 'departures'

Use of some of my pictures if it doesn't look too busy.
Should not have
• Anything too over the top.

```html
<!DOCTYPE html>
<html lang="en">
<head>
<meta charset="utf-8">
<title>Travel Departures Poster</title>
<link rel="stylesheet" href="https://fonts.googleapis.com/css2?family=Oswald:wght@500;600&family=Noto+Serif:ital@0;1&display=swap">
<style>
  :root {
    --page: #ffffff;
    --board: #1c1c1c;
    --flap: #2b2b2b;
    --flap-line: #0c0c0c;
    --sign-yellow: #f9ec2f;
    --flap-yellow: #f4e630;
    --flap-white: #f2f2f2;
    --ink: #111111;
  }
  * { box-sizing: border-box; margin: 0; padding: 0; }
  html, body { width: 1200px; height: 1000px; overflow: hidden; background: var(--page); }
  .poster { position: absolute; left: 287px; top: 50px; width: 633px; height: 898px; background: var(--page); overflow: hidden; }
  .photo { position: absolute; }
  .photo--framed { border: 4px solid var(--page); }
  .photo--temple { left: 381px; top: 175px; width: 252px; height: 212px; background: linear-gradient(180deg, #c9ccd0 0%, #6f7a70 45%, #2f4a2e 100%); }
  .photo--canal { left: 443px; top: 385px; width: 190px; height: 152px; background: linear-gradient(180deg, #cfe0ea 0%, #d9cdb8 40%, #3c4a50 100%); }
  .photo--parade { left: 379px; top: 500px; width: 150px; height: 126px; transform: rotate(-2.5deg); background: linear-gradient(160deg, #e8d8c0 0%, #c9513a 55%, #e9c34a 100%); }
  .photo--bay { left: 189px; top: 538px; width: 444px; height: 360px; background: linear-gradient(180deg, #5b9ed6 0%, #9cc3de 30%, #4f6b3f 52%, #5f9a92 70%, #c8b48f 100%); }
  .photo--market { left: 0; top: 645px; width: 185px; height: 253px; background: linear-gradient(180deg, #6a6b6e 0%, #5b6f8a 45%, #8a7a5a 75%, #d9d6cf 100%); }

  .board { position: absolute; left: 24px; top: 26px; width: 350px; height: 614px; background: var(--board); border: 2px solid var(--page); }
  .board__header { height: 77px; background: var(--sign-yellow); display: flex; align-items: center; justify-content: center; font-family: "Oswald", sans-serif; font-weight: 600; font-size: 23px; color: var(--ink); letter-spacing: -0.3px; }
  .board__rows { list-style: none; }
  .board__row {
    height: 38.3px; line-height: 38.3px; padding-left: 8px; white-space: nowrap;
    font-family: "Oswald", sans-serif; font-weight: 500; font-size: 25px; letter-spacing: 11.5px;
    background:
      linear-gradient(180deg, transparent 18px, var(--flap-line) 18px, var(--flap-line) 20px, transparent 20px),
      repeating-linear-gradient(90deg, var(--flap) 0, var(--flap) 22px, var(--board) 22px, var(--board) 24.5px);
    border-bottom: 1px solid #000;
  }
  .board__place { color: var(--flap-yellow); }
  .board__year { color: var(--flap-white); }

  .quote { position: absolute; left: 378px; top: 24px; width: 255px; text-align: center; font-family: "Noto Serif", serif; font-style: italic; font-size: 21px; line-height: 25px; color: var(--ink); }
  .quote__source { position: absolute; right: 26px; top: 136px; font-family: "Noto Serif", serif; font-size: 15px; color: var(--ink); }
</style>
</head>
<body>
  <main class="poster">
    <div class="photo photo--bay" role="img" aria-label="Photo of a limestone sea stack in a tropical bay with longtail boats on the beach"></div>
    <div class="photo photo--market" role="img" aria-label="Photo of a market vendor in a conical hat with a basket of eggs"></div>
    <div class="photo photo--temple" role="img" aria-label="Photo of a giant seated bronze statue atop long stairs among trees"></div>
    <div class="photo photo--canal photo--framed" role="img" aria-label="Photo of three friends by a canal in an Italian town"></div>
    <div class="photo photo--parade photo--framed" role="img" aria-label="Photo of children at a lion dance festival"></div>

    <section class="board" aria-label="Travel history">
      <h1 class="board__header">DEPARTURES/ARRIVALS</h1>
      <ul class="board__rows">
        <li class="board__row"><span class="board__place">USA </span><span class="board__year">2003</span></li>
        <li class="board__row"><span class="board__place">MALAYSIA </span><span class="board__year">2006</span></li>
        <li class="board__row"><span class="board__place">THAILAND </span><span class="board__year">2007</span></li>
        <li class="board__row"><span class="board__place">ITALY </span><span class="board__year">2009</span></li>
        <li class="board__row"><span class="board__place">INDIA </span><span class="board__year">2010</span></li>
        <li class="board__row"><span class="board__place">VIETNAM </span><span class="board__year">2010</span></li>
        <li class="board__row"><span class="board__place">HONG KONG </span><span class="board__year">2010</span></li>
        <li class="board__row"><span class="board__place">BALI </span><span class="board__year">2011</span></li>
        <li class="board__row"><span class="board__place">MALAYSIA </span><span class="board__year">2012</span></li>
        <li class="board__row"><span class="board__place">SINGAPORE </span><span class="board__year">2012</span></li>
        <li class="board__row"><span class="board__place">VIETNAM </span><span class="board__year">2013</span></li>
        <li class="board__row"><span class="board__place">CAMBODIA </span><span class="board__year">2013</span></li>
        <li class="board__row"><span class="board__place">LAOS </span><span class="board__year">2013</span></li>
        <li class="board__row"><span class="board__place">EUROPE </span><span class="board__year">2015</span></li>
      </ul>
    </section>

    <blockquote class="quote">“The world is a book and those who do not travel read only one page.”</blockquote>
    <p class="quote__source">Severin of Tallowmere</p>
  </main>
</body>
</html>
```